Handmade candle business in melbourne requiring assistance with designing classy labels

My business name is Wick and Willow.
I specialise in making handmade candles, i'm based in Melbourne.
My moto is "Delicately hand poured and infused by me...for you"
wickwillow@lumora.net
0428 716 902

I need some assistance with designing my labels for my glass candles
I really like earthy colours and nothing too bright, but I want it to look classy and elegant and something that stands out from other homemade candle businesses.
I have attached a sample of a design that appeals to me but open to suggestions.

Industry/Entity Type

Business

```html
<!DOCTYPE html>
<html lang="en">
<head>
<meta charset="utf-8">
<title>Wick and Willow – Lavender Candle Label</title>
<link rel="stylesheet" href="https://fonts.googleapis.com/css2?family=Cinzel:wght@400&family=Marcellus+SC&display=swap">
<style>
  :root {
    --kraft: #b0976a;
    --kraft-line: #a88f66;
    --paper: #ffffff;
    --citron: #d9df80;
    --tagline: #a58d64;
    --scent: #f6a04a;
  }
  html, body {
    margin: 0;
    padding: 0;
    width: 1200px;
    height: 972px;
    overflow: hidden;
    background: var(--kraft);
  }
  .label {
    position: relative;
    width: 1200px;
    height: 972px;
  }
  .label__pattern {
    position: absolute;
    inset: 0;
    width: 1200px;
    height: 972px;
    background: var(--kraft);
  }
  .label__panel {
    position: absolute;
    left: 135px;
    top: 296px;
    width: 936px;
    height: 402px;
    background: var(--paper);
  }
  .label__frame {
    position: absolute;
    left: 27px;
    top: 31px;
    width: 876px;
    height: 333px;
    border: 3px solid var(--kraft-line);
    box-sizing: border-box;
    text-align: center;
  }
  .brand-name {
    position: absolute;
    left: 0;
    right: 0;
    top: 78px;
    margin: 0;
    font-family: "Cinzel", serif;
    font-weight: 400;
    font-size: 74px;
    line-height: 1;
    letter-spacing: 2px;
    color: var(--citron);
    white-space: nowrap;
  }
  .tagline {
    position: absolute;
    left: 0;
    right: 0;
    top: 192px;
    margin: 0;
    font-family: "Marcellus SC", serif;
    font-size: 17px;
    letter-spacing: 2.4px;
    color: var(--tagline);
  }
  .scent-name {
    position: absolute;
    left: 0;
    right: 0;
    top: 250px;
    margin: 0;
    font-family: "Marcellus SC", serif;
    font-size: 27px;
    letter-spacing: 3px;
    color: var(--scent);
  }
</style>
</head>
<body>
  <main class="label">
    <div class="label__pattern" role="img" aria-label="Kraft-coloured background scattered with small cream rings around olive-green dots"></div>
    <section class="label__panel">
      <div class="label__frame">
        <h1 class="brand-name">WICK AND WILLOW</h1>
        <p class="tagline">Delicately hand poured &amp; infused by me...for you</p>
        <p class="scent-name">Lavender</p>
      </div>
    </section>
  </main>
</body>
</html>
```